Kindle Book Cover for Teen Financial Niche

Had a temporary cover done for the book but it needs a lot better cover now it is starting to get some traction.
The current book can be seen here:
https://www.bookvalemart.com/dp/Q7K42LZ9RT
I am wanting something very different if possible. Please search books in the teen financial niche on Bookvale and you will see that a lot of the covers are very similar in style.
I am looking for something different that will stand out in a crowded marketplace.
If you are putting someone on the cover please use a male character rather than a female one.
Thanks
Dale

```html
<!DOCTYPE html>
<html lang="en">
<head>
<meta charset="utf-8">
<title>Everyday Capital – Book Cover</title>
<link rel="stylesheet" href="https://fonts.googleapis.com/css2?family=Oswald:wght@700&family=Libre+Baskerville:ital,wght@1,400;1,700&family=Montserrat:wght@600&display=swap">
<style>
  :root {
    --ink: #000000;
    --paper: #ffffff;
    --accent: #ffff00;
    --rule: #bdbdbd;
    --photo-light: #8a8a8a;
    --photo-mid: #3a3a3a;
  }
  * { margin: 0; padding: 0; box-sizing: border-box; }
  html, body { width: 848px; height: 1200px; overflow: hidden; background: var(--ink); }
  .cover { position: relative; width: 848px; height: 1200px; background: var(--ink); overflow: hidden; }

  .series-ribbon { position: absolute; left: 224px; top: 63px; width: 402px; height: 62px; }
  .series-name {
    position: absolute; left: 224px; top: 63px; width: 402px; height: 62px;
    display: flex; align-items: center; justify-content: center;
    font-family: "Libre Baskerville", serif; font-style: italic; font-weight: 400;
    font-size: 37px; letter-spacing: 1.5px; color: var(--ink);
  }

  .title-art { position: absolute; left: 0; top: 140px; width: 848px; height: 310px; }
  .title-word { font-family: "Oswald", sans-serif; font-weight: 700; }
  .title-top { fill: var(--paper); }
  .title-main { fill: var(--accent); }

  .divider {
    position: absolute; left: 120px; width: 612px; height: 2px;
    background: linear-gradient(90deg, transparent, var(--rule) 25%, var(--paper) 50%, var(--rule) 75%, transparent);
  }
  .divider-top { top: 476px; }
  .divider-bottom { top: 624px; }

  .subtitle {
    position: absolute; left: 0; top: 488px; width: 848px; text-align: center;
    font-family: "Libre Baskerville", serif; font-style: italic;
    font-size: 32px; line-height: 39.5px; letter-spacing: 3px; color: var(--paper);
  }
  .subtitle .hl { color: var(--accent); }
  .subtitle .strong { font-weight: 700; }
  .subtitle .plain { font-weight: 400; }

  .audience-stroke { position: absolute; left: 162px; top: 659px; width: 525px; height: 46px; }
  .audience {
    position: absolute; left: 162px; top: 659px; width: 525px; height: 46px;
    display: flex; align-items: center; justify-content: center;
    font-family: "Libre Baskerville", serif; font-style: italic; font-weight: 700;
    font-size: 22px; letter-spacing: 1px; color: var(--ink);
  }

  .cover-photo {
    position: absolute; left: 60px; top: 735px; width: 728px; height: 400px;
    background: radial-gradient(ellipse 55% 50% at 52% 45%, var(--photo-light) 0%, var(--photo-mid) 55%, var(--ink) 100%);
  }

  .author-band {
    position: absolute; left: 0; top: 1135px; width: 848px; height: 65px;
    background: var(--accent);
    display: flex; align-items: center; justify-content: center;
  }
  .author-name {
    font-family: "Montserrat", sans-serif; font-weight: 600;
    font-size: 27px; letter-spacing: 17px; padding-left: 17px; color: var(--ink);
  }
</style>
</head>
<body>
<main class="cover">
  <svg class="series-ribbon" viewBox="0 0 402 62" aria-hidden="true">
    <polygon points="0,0 402,0 381,31 402,62 0,62 21,31" fill="var(--accent)"/>
  </svg>
  <div class="series-name">Cash Compass</div>

  <svg class="title-art" viewBox="0 0 848 310" aria-label="Everyday Capital">
    <text class="title-word title-top" x="124" y="120" textLength="603" lengthAdjust="spacingAndGlyphs" font-size="136">EVERYDAY</text>
    <text class="title-word title-main" x="68" y="294" textLength="713" lengthAdjust="spacingAndGlyphs" font-size="199">CAPITAL</text>
  </svg>

  <div class="divider divider-top"></div>
  <p class="subtitle">
    <span class="plain">A Guide to:</span> <span class="hl strong">Boosting Income,</span><br>
    <span class="strong">Planning,</span> <span class="hl plain">Smart Spending,</span><br>
    <span class="hl strong">Saving</span> <span class="plain">and</span> <span class="hl strong">Growing Wealth</span>
  </p>
  <div class="divider divider-bottom"></div>

  <svg class="audience-stroke" viewBox="0 0 525 46" aria-hidden="true">
    <path d="M16,4 L500,2 L508,8 L502,13 L516,19 L507,26 L521,35 L512,43 L32,45 L22,40 L4,35 L18,29 L0,22 L16,15 L6,9 Z" fill="var(--accent)"/>
  </svg>
  <div class="audience">FOR TEENS AND YOUNG ADULTS</div>

  <div class="cover-photo" role="img" aria-label="Black and white photo of two hands fanning out a thick stack of banknotes"></div>

  <div class="author-band">
    <span class="author-name">OWEN CASTELL</span>
  </div>
</main>
</body>
</html>
```